Business Card design for construction company

I would like a business card design for a construction company - Harlow Constructions. I have attached the ai logo file for use. I would like the card to be very smart and clean and incorporate only white and the two colours in the logo. I would like the card to have two sides. One side can just have the logo, the other with the relevant information.

Target Market(s)

Building and Construction Clients

Industry/Entity Type

Business

Contact Information for Business Card

Name: Tom Pardoe
Company: Harlow Constructions Pty Limited
Address: 14 Mallee Crescent Carrow Vale 2093
Phone: 0427 531 068
Email: tomp@harlowbuild-example.com.au

Font styles to use
Serif
Sans Serif

Requirements
Must have
• Details noted above
• Logo as provided
• Colours as in logo
• Square edges
• A font that compliments the logo
Should not have
• Any colour other than white and those in logo
• Rounded edges

```html
<!DOCTYPE html>
<html lang="en">
<head>
<meta charset="utf-8">
<title>Harlow Constructions – Business Card</title>
<link rel="stylesheet" href="https://fonts.googleapis.com/css2?family=Oswald:wght@500&family=Exo+2:wght@400&display=swap">
<style>
  :root {
    --backdrop: #2a2b2d;
    --card: #ffffff;
    --brand-blue: #1ba0dd;
    --brand-grey: #4a4d52;
    --muted: #5c5f64;
  }
  * { box-sizing: border-box; margin: 0; padding: 0; }
  html, body {
    width: 1200px;
    height: 780px;
    overflow: hidden;
    background: var(--backdrop);
  }
  .sheet {
    width: 1200px;
    height: 780px;
    display: flex;
    align-items: center;
    justify-content: center;
    gap: 50px;
  }
  .card {
    width: 525px;
    height: 300px;
    background: var(--card);
    position: relative;
    display: flex;
    align-items: center;
    justify-content: center;
  }
  /* Front side */
  .wordmark {
    display: flex;
    align-items: center;
    gap: 14px;
  }
  .wordmark-dot {
    width: 10px;
    height: 10px;
    background: var(--brand-blue);
  }
  .wordmark-name {
    font-family: "Exo 2", sans-serif;
    font-weight: 400;
    font-size: 22px;
    letter-spacing: 3px;
    text-transform: uppercase;
    color: var(--brand-grey);
  }
  /* Back side */
  .details {
    display: flex;
    align-items: center;
    gap: 16px;
  }
  .identity {
    text-align: right;
  }
  .person-name {
    font-family: "Oswald", sans-serif;
    font-weight: 500;
    font-size: 30px;
    line-height: 1;
    letter-spacing: 0.5px;
    color: var(--brand-blue);
    text-transform: uppercase;
  }
  .person-role {
    font-family: "Exo 2", sans-serif;
    font-size: 12px;
    color: var(--muted);
    margin-top: 2px;
  }
  .divider {
    width: 2px;
    height: 58px;
    background: var(--brand-blue);
  }
  .contact {
    font-family: "Exo 2", sans-serif;
    font-size: 11.5px;
    line-height: 1.35;
    color: var(--brand-grey);
    letter-spacing: 0.3px;
  }
  .contact-address { margin-bottom: 3px; }
  .contact-line {
    display: flex;
    align-items: center;
    gap: 7px;
  }
  .contact-line svg { flex: none; }
</style>
</head>
<body>
  <main class="sheet">
    <section class="card card-front" aria-label="Card front">
      <div class="wordmark">
        <span class="wordmark-dot"></span>
        <span class="wordmark-name">Harlow Constructions</span>
      </div>
    </section>

    <section class="card card-back" aria-label="Card back">
      <div class="details">
        <div class="identity">
          <p class="person-name">Tom Pardoe</p>
          <p class="person-role">Founder</p>
        </div>
        <span class="divider"></span>
        <div class="contact">
          <p class="contact-address">14 Mallee Crescent<br>Carrow Vale 2093</p>
          <p class="contact-line">
            <svg width="9" height="10" viewBox="0 0 24 24" aria-hidden="true"><path fill="#1ba0dd" d="M6.6 10.8a15.1 15.1 0 0 0 6.6 6.6l2.2-2.2c.3-.3.7-.4 1-.2 1.1.4 2.3.6 3.6.6.6 0 1 .4 1 1V20c0 .6-.4 1-1 1A17 17 0 0 1 3 4c0-.6.4-1 1-1h3.5c.6 0 1 .4 1 1 0 1.3.2 2.5.6 3.6.1.3 0 .7-.2 1z"/></svg>
            <span>0427 531 068</span>
          </p>
          <p class="contact-line">
            <svg width="10" height="8" viewBox="0 0 20 14" aria-hidden="true"><rect x="1" y="1" width="18" height="12" fill="none" stroke="#1ba0dd" stroke-width="2"/><path d="M1 1l9 7 9-7" fill="none" stroke="#1ba0dd" stroke-width="2"/></svg>
            <span>tomp@harlowbuild-example.com.au</span>
          </p>
        </div>
      </div>
    </section>
  </main>
</body>
</html>
```